Your Harbor Weekend book cover design

I have attached an image that I would like this front cover to be similar to. This is a book about marriage so there will need to be a man and woman on the front cover and I am open to your creative design from that point. I have also attached the ISBN barcode and photo of authors for back cover. Book details are below:

Title:
Your HARBOR WEEKEND
Tending Wedlock
A Handbook for Your Home and Household

Authors: LEN AND MAVE’ HOLBURN
Book size : 8x10
Back cover text:
LEN AND MAVE’ HOLBURN

Authors, parents, grandparents, business owners, and public speakers, has served in ministry for over 25 years. They are the founders of Stand Firm Global Fellowship, serving as the senior pastors. They are also currently serving as national and international mission directors. They both are very intentional about assisting couples in developing their marriages. Having firsthand knowledge of God’s mercy in this area, the Holburns are sharing the power of Tending Wedlock with dedication and simplicity.

They are blessed to have three married children, and thirteen grandchildren in their more than 40 years of marriage. They are currently residing in Birmingham, Alabama. They look forward seeing you soon.

Back cover photo: Attached

```html
<!DOCTYPE html>
<html lang="en">
<head>
<meta charset="utf-8">
<title>Your Harbor Weekend — Book Cover</title>
<link rel="stylesheet" href="https://fonts.googleapis.com/css2?family=Cinzel:wght@400;500&family=Josefin+Sans:wght@400&display=swap">
<style>
  :root {
    --page-bg: #efe8e4;
    --cover-pink: #e2bcb1;
    --ink: #1b1515;
    --art-cream: #f6e2d2;
    --art-peach: #f0b9a0;
    --art-teal: #2f6f6c;
    --art-sage: #8fb8aa;
  }
  * { margin: 0; padding: 0; box-sizing: border-box; }
  html, body {
    width: 1200px;
    height: 1200px;
    overflow: hidden;
    background: var(--page-bg);
  }
  .book-cover {
    position: absolute;
    left: 160px;
    top: 50px;
    width: 880px;
    height: 1100px;
    background: var(--cover-pink);
    color: var(--ink);
    text-align: center;
  }
  .book-title {
    position: absolute;
    top: 70px;
    left: 0;
    width: 100%;
    font-family: "Cinzel", serif;
    font-weight: 400;
    font-size: 76px;
    line-height: 100px;
    letter-spacing: 0.14em;
    padding-left: 0.14em;
  }
  .book-subtitle {
    position: absolute;
    top: 286px;
    left: 0;
    width: 100%;
    font-family: "Josefin Sans", sans-serif;
    font-size: 21px;
    letter-spacing: 0.2em;
    padding-left: 0.2em;
    text-transform: uppercase;
  }
  .cover-art {
    position: absolute;
    left: 250px;
    top: 375px;
    width: 380px;
    height: 435px;
  }
  .book-tagline {
    position: absolute;
    top: 864px;
    left: 0;
    width: 100%;
    font-family: "Josefin Sans", sans-serif;
    font-size: 22px;
    line-height: 30px;
    letter-spacing: 0.28em;
    padding-left: 0.28em;
    text-transform: uppercase;
  }
  .book-authors {
    position: absolute;
    top: 950px;
    left: 0;
    width: 100%;
    font-family: "Cinzel", serif;
    font-weight: 500;
    font-size: 37px;
    letter-spacing: 0.1em;
    padding-left: 0.1em;
  }
</style>
</head>
<body>
  <main class="book-cover">
    <h1 class="book-title">YOUR HARBOR<br>WEEKEND</h1>
    <p class="book-subtitle">Tending Wedlock</p>

    <svg class="cover-art" viewBox="0 0 380 435" role="img" aria-label="Illustration of a man and woman facing each other in soft pastel leaf shapes">
      <defs>
        <linearGradient id="artGradient" x1="0" y1="0" x2="1" y2="1">
          <stop offset="0" stop-color="var(--art-teal)"/>
          <stop offset="0.35" stop-color="var(--art-cream)"/>
          <stop offset="0.7" stop-color="var(--art-peach)"/>
          <stop offset="1" stop-color="var(--art-sage)"/>
        </linearGradient>
      </defs>
      <path d="M60 70 C110 10 250 -5 320 60 C370 110 350 180 360 250 C372 330 330 420 240 428 C160 436 70 425 40 360 C10 300 50 250 25 190 C5 140 20 110 60 70 Z" fill="url(#artGradient)" opacity="0.9"/>
    </svg>

    <p class="book-tagline">A Handbook for Your<br>Home and Household</p>
    <p class="book-authors">LEN AND MAVE’ HOLBURN</p>
  </main>
</body>
</html>
```